Civic Shieldpoint Company

We have design at www.vexaloft.com and want
New site design
Carallax
Images added
Were looking for your eyes. Just placement and look and feel. No hard coding. Design only.

Industry/Entity Type

It Company

```html
<!DOCTYPE html>
<html lang="en">
<head>
<meta charset="utf-8">
<title>Vexaloft — Protect Your Identity</title>
<link rel="stylesheet" href="https://fonts.googleapis.com/css2?family=Roboto:wght@400;700&family=Roboto+Slab:wght@300&display=swap">
<style>
  :root {
    --ink: #000000;
    --paper: #ffffff;
    --accent: #ff0000;
    --hero-light: #e9ece4;
    --hero-warm: #d9b9a4;
    --hero-green: #a9c48c;
    --hero-blue: #b5c3cf;
    --marker: #8a8a8a;
  }
  * { margin: 0; padding: 0; box-sizing: border-box; }
  html, body { width: 1200px; height: 820px; overflow: hidden; background: var(--paper); }
  body { font-family: "Roboto", Arial, sans-serif; position: relative; }

  .site-header {
    position: absolute; left: 0; top: 0; width: 1200px; height: 65px;
    background: var(--ink);
  }
  .brand {
    position: absolute; left: 150px; top: 14px;
    color: var(--paper); font-weight: 700; font-size: 28px; letter-spacing: 0.5px;
    line-height: 36px;
  }
  .signin {
    position: absolute; left: 820px; top: 22px;
    display: flex; align-items: center; gap: 6px;
    color: var(--paper); font-size: 11px; font-weight: 700; line-height: 20px;
  }
  .cta {
    position: absolute; left: 886px; top: 14px; width: 164px; height: 38px;
    background: var(--accent); color: var(--paper);
    font-weight: 700; font-size: 18px; line-height: 38px; text-align: center;
  }

  .hero {
    position: absolute; left: 0; top: 65px; width: 1200px; height: 622px; overflow: hidden;
  }
  .hero-photo {
    position: absolute; inset: 0;
    background:
      radial-gradient(ellipse 320px 400px at 360px 380px, var(--hero-warm), transparent 70%),
      radial-gradient(ellipse 200px 300px at 690px 260px, var(--hero-green), transparent 70%),
      radial-gradient(ellipse 320px 380px at 900px 420px, var(--hero-blue), transparent 70%),
      linear-gradient(90deg, #f3f3f0 0%, var(--hero-light) 50%, #c8d6b2 100%);
  }
  .hero-title {
    position: absolute; left: 0; top: 288px; width: 1200px; text-align: center;
    color: var(--paper); font-weight: 700; font-size: 76px; line-height: 90px;
  }
  .play-button { position: absolute; left: 544px; top: 378px; }
  .slide-markers {
    position: absolute; left: 1165px; top: 310px;
    display: flex; flex-direction: column; gap: 13px;
  }

  .features-title {
    position: absolute; left: 0; top: 765px; width: 1200px; text-align: center;
    font-family: "Roboto Slab", Georgia, serif; font-weight: 300; font-size: 62px;
    letter-spacing: 2px; color: var(--ink); line-height: 70px;
  }
</style>
</head>
<body>
  <header class="site-header">
    <div class="brand">Vexaloft</div>
    <div class="signin">
      <svg width="16" height="15" viewBox="0 0 16 15" aria-hidden="true">
        <circle cx="8" cy="4.5" r="4" fill="#fff"/>
        <path d="M0 15 C0 10 4 9 8 9 C12 9 16 10 16 15 Z" fill="#fff"/>
      </svg>
      <span>Signin</span>
    </div>
    <a class="cta">Get Started NOW!</a>
  </header>

  <section class="hero">
    <div class="hero-photo" role="img" aria-label="Photo of a smiling family of four outdoors, children on the parents' backs"></div>
    <h1 class="hero-title">Protect Your Identity</h1>
    <svg class="play-button" width="114" height="114" viewBox="0 0 114 114" aria-label="Play video">
      <circle cx="57" cy="57" r="54" fill="none" stroke="#fff" stroke-width="3"/>
      <path d="M43 33 L87 57 L43 81 Z" fill="#fff"/>
    </svg>
    <div class="slide-markers" aria-hidden="true">
      <svg width="14" height="13"><path d="M0 0 H14 L7 13 Z" fill="#8a8a8a"/></svg>
      <svg width="14" height="13"><path d="M0 0 H14 L7 13 Z" fill="#8a8a8a"/></svg>
      <svg width="14" height="13"><path d="M0 0 H14 L7 13 Z" fill="#8a8a8a"/></svg>
      <svg width="14" height="13"><path d="M0 0 H14 L7 13 Z" fill="#8a8a8a"/></svg>
      <svg width="14" height="13"><path d="M0 0 H14 L7 13 Z" fill="#8a8a8a"/></svg>
      <svg width="14" height="13"><path d="M0 0 H14 L7 13 Z" fill="#8a8a8a"/></svg>
    </div>
  </section>

  <h2 class="features-title">FEATURES</h2>
</body>
</html>
```